Tavrex Inc.
Business Cards and Stationery - Social Media
Business Cards and Stationery
Karim Dallouf
Managing Director
P.O. Box 918 Manama Kingdom of Bahrain
k@tavrexbh.com
tavrexbh.com
icons for phone & cell instead of text. add twitter icon with @TavrexBH add skype icon with kDallouf the backside of the busniess card will have the logo and the website below it. and below those: Web Design | Social Networks | Innovations

```html
<!DOCTYPE html>
<html lang="en">
<head>
<meta charset="utf-8">
<title>Tavrex Inc. – Business Cards</title>
<link rel="stylesheet" href="https://fonts.googleapis.com/css2?family=Open+Sans:wght@400;600;700;800&display=swap">
<style>
  :root {
    --bg: #d9d9d9;
    --red: #d7141a;
    --red-deep: #8c0a0d;
    --red-bright: #ee2a2a;
    --ink: #4a4a4a;
    --ink-soft: #7a7a7a;
    --mark: #3c3c3c;
    --white: #ffffff;
  }
  * { margin: 0; padding: 0; box-sizing: border-box; }
  html, body { width: 1200px; height: 901px; overflow: hidden; }
  body {
    background: var(--bg);
    font-family: "Open Sans", Arial, sans-serif;
    position: relative;
  }
  .card {
    position: absolute;
    top: 302px;
    width: 520px;
    height: 297px;
    border-radius: 3px;
    box-shadow: 0 10px 28px rgba(0,0,0,.22);
    overflow: hidden;
  }
  /* Back side */
  .card-back {
    left: 60px;
    background: radial-gradient(ellipse at 50% 45%, var(--red-bright) 0%, var(--red) 45%, var(--red-deep) 100%);
    color: var(--white);
    display: flex;
    flex-direction: column;
    align-items: center;
    justify-content: center;
    text-align: center;
  }
  .back-brand {
    display: flex;
    align-items: center;
    gap: 12px;
    font-weight: 800;
    font-size: 30px;
    letter-spacing: .5px;
  }
  .back-brand .brand-dot {
    width: 46px; height: 46px; border-radius: 50%;
    background: var(--white);
  }
  .back-web { margin-top: 14px; font-size: 15px; font-weight: 400; }
  .back-services { margin-top: 26px; font-size: 13px; letter-spacing: .3px; }

  /* Front side */
  .card-front {
    left: 620px;
    background: linear-gradient(135deg, #ffffff 0%, #f6f6f6 100%);
    color: var(--ink);
    padding: 30px 34px;
  }
  .front-brand {
    display: flex;
    align-items: center;
    gap: 12px;
    font-weight: 800;
    font-size: 30px;
    color: var(--red);
    letter-spacing: .5px;
  }
  .front-brand .brand-dot {
    width: 48px; height: 48px; border-radius: 50%;
    background: var(--mark);
  }
  .contact { margin: 22px 0 0 118px; }
  .person-name { color: var(--red); font-weight: 700; font-size: 16px; }
  .person-title { color: var(--ink-soft); font-size: 10px; margin-top: 1px; }
  .address { margin-top: 12px; font-size: 10px; line-height: 1.45; color: var(--ink); }
  .channels { list-style: none; margin-top: 8px; font-size: 10px; line-height: 1.55; }
  .channels li { display: flex; align-items: center; gap: 6px; }
  .channels svg { width: 10px; height: 10px; flex: none; }
</style>
</head>
<body>

<section class="card card-back" aria-label="Business card back">
  <div class="back-brand"><span class="brand-dot"></span><span>Tavrex Inc.</span></div>
  <p class="back-web">www.tavrexbh.com</p>
  <p class="back-services">Web Design | Social Networks | Innovations</p>
</section>

<section class="card card-front" aria-label="Business card front">
  <div class="front-brand"><span class="brand-dot"></span><span>Tavrex Inc.</span></div>
  <div class="contact">
    <p class="person-name">Karim Dallouf</p>
    <p class="person-title">Managing Director</p>
    <p class="address">P.O. Box 918<br>Manama<br>Kingdom of Bahrain</p>
    <ul class="channels">
      <li>
        <svg viewBox="0 0 10 10"><path d="M2 1h2l1 2-1.2 1a5 5 0 0 0 2.2 2.2L7 5l2 1v2a1 1 0 0 1-1 1A7 7 0 0 1 1 2a1 1 0 0 1 1-1z" fill="var(--red)"/></svg>
        +973 1755 0192
      </li>
      <li>
        <svg viewBox="0 0 10 10"><rect x="2.5" y="0.5" width="5" height="9" rx="1" fill="var(--red)"/><rect x="3.5" y="1.8" width="3" height="5" fill="#fff"/></svg>
        +973 3966 4810
      </li>
      <li>
        <svg viewBox="0 0 10 10"><circle cx="5" cy="5" r="4.5" fill="var(--red)"/></svg>
        @TavrexBH
      </li>
      <li>
        <svg viewBox="0 0 10 10"><rect x="0.5" y="0.5" width="9" height="9" rx="2" fill="var(--red)"/></svg>
        kDallouf
      </li>
      <li>
        <svg viewBox="0 0 10 10"><rect x="0.5" y="2" width="9" height="6.5" fill="var(--red)"/><path d="M0.8 2.3 5 5.6 9.2 2.3" stroke="#fff" stroke-width="0.9" fill="none"/></svg>
        k@tavrexbh.com
      </li>
      <li>
        <svg viewBox="0 0 10 10"><circle cx="5" cy="5" r="4.2" fill="none" stroke="var(--red)" stroke-width="1.2"/><path d="M1 5h8M5 1c-2 2.5-2 5.5 0 8M5 1c2 2.5 2 5.5 0 8" stroke="var(--red)" stroke-width=".8" fill="none"/></svg>
        www.tavrexbh.com
      </li>
    </ul>
  </div>
</section>

</body>
</html>
```